High-end Oceanfront Real Estate Group Needs Clean, Modern Web Design

I’m looking for a clean, professional, modern and beautiful homepage web design for a Real Estate group in Southern California, USA.

The group/company is “Marlow on the Shore,” and they specialize in high end (i.e. expensive), oceanfront real estate in the Orange County area.

The look and feel of the page should accentuate the brand qualities: luxurious/expensive, professional, and beautiful (Orange County is one of the most beautiful areas in all the US and we would love the site to emphasize the beautiful beaches and scenery it has to offer).

Looks we like:
• www.brantleyhomesrealty.example
• www.keptbyfenwick.example -- I think the design is pretty out-dated in this site, but I like the organization/layout of the site

Header Tags (I don’t know if we can fit all of these, may need a side-menu, but I’d prefer header title only if possible):
• Welcome
• Featured Listings
• Previously Sold
• Sell
• Property Search
• Team
• Videos
• Blog
• Explore O.C.
• Contact

I have attached the beach and logo pics that we would like to use as the header, a few pictures of the team, and one sample home/view pic which can be used in any of the other sections (for pictures of the homes, just find expensive oceanfront houses and that will be fine).

I promise to provide feedback to each and every design submission. I appreciate the hard work that all of you are putting into your designs. There can be only one contest winner, but I hope to give all of you helpful feedback to submit the best designs possible!

Target Market(s)

Very wealthy home owners of oceanfront properties. These properties are worth several millions of dollars, and thus the site and brand needs to be targeted to very wealthy, successful individuals and families (both US and international buyers).

Industry/Entity Type

Real Estate

Number of Pages Required

2 page

Requirements
Must have
• I don’t want to give too many requirements, because I want to let you all be creative. However, here are the few Must Haves:
• Must submit 2 page designs (a home page and a sub page)
• Must use logo provided
• Focus is mostly on homes, but I would like to include some beach/ocean imagery as well
• The first “item” on the home page should be an accordion/slider which shows pictures of homes and with 1 line of text: “List with the Leader” and two link buttons: “Sell Your Home” and “Buy Your Home”
• Color palette needs to be mainly blues--to match ocean and sky blue
• Exported in all major formats (psd,ai,eps,png,jpeg,etc)
Nice to have
• We don’t necessarily need all of these, but would like to feature most:
• List of videos
• “Meet the Team”—brief team bios and pics
• Link(s) to Blog
• “List with the Leader” – section on why they should choose this firm
• Featured Listings
• Previously Sold

```html
<!DOCTYPE html>
<html lang="en">
<head>
<meta charset="utf-8">
<title>Marlow on the Shore — Team &amp; Blog</title>
<link href="https://fonts.googleapis.com/css2?family=Arvo:wght@400;700&family=Raleway:wght@400;500;600;700&display=swap" rel="stylesheet">
<style>
:root{
  --ink:#222;
  --text:#444;
  --muted:#555;
  --panel:#4a4a4a;
  --panel-stripe:#6d8fae;
  --top-rule:#4d6c8c;
  --date-blue:#3f82b8;
  --date-line:#6fa3cc;
  --accent:#009fef;
  --accent-text:#4fc3f7;
  --footer:#4a4a4a;
  --footer-field:#3c3c3c;
  --footer-bottom:#3b3b3b;
  --footer-text:#e6e6e6;
  --footer-head:#bdbdbd;
  --white:#fff;
}
*{margin:0;padding:0;box-sizing:border-box}
html,body{width:1092px;height:1200px;overflow:hidden;background:var(--white)}
body{position:relative;font-family:'Raleway',sans-serif;color:var(--text)}
h1,h2,h3,h4{font-weight:400}
.abs{position:absolute}
.top-rule{left:0;top:0;width:1092px;height:5px;background:var(--top-rule)}
.section-title{left:0;width:1092px;text-align:center;font-family:'Arvo',serif;font-size:35px;color:var(--ink);line-height:1}
.section-sub{left:0;width:1092px;text-align:center;font-size:17px;color:var(--muted);line-height:1}

/* team */
.team-shapes{left:0;top:160px}
.photo{border-radius:80px 80px 0 0}
.photo-left{left:150px;top:190px;width:164px;height:287px;background:linear-gradient(180deg,#d9c3ae 0%,#8a7a6c 35%,#6e6458 100%)}
.photo-right{left:776px;top:202px;width:158px;height:275px;background:linear-gradient(180deg,#e6cf9e 0%,#e8c6b0 40%,#d7b29b 100%)}
.member{width:200px;text-align:center;color:var(--white)}
.member-name{font-family:'Arvo',serif;font-size:19px;line-height:20px}
.member-bio{font-size:11px;line-height:14.7px;margin-top:12px;white-space:nowrap}
.member-more{font-size:11.5px;font-weight:700;margin-top:14px;line-height:14px}
.socials{display:flex;justify-content:center;gap:13px;margin-top:32px}
.socials span{width:25px;height:25px;border:1.5px solid var(--white);border-radius:50%}

/* blog */
.blog{left:0;top:477px;width:1092px;height:455px;background:linear-gradient(180deg,#cfe3f4 0%,#e9f2fa 35%,#f4f8fc 60%,#eef4f8 100%)}
.post-meta{width:57px;height:169px;background:var(--date-blue);color:var(--white);text-align:center}
.meta-date{height:51px;border-bottom:1px solid var(--date-line);padding-top:7px}
.meta-day{font-size:22px;font-weight:600;line-height:1}
.meta-month{font-size:11px;line-height:1.1}
.meta-row{height:39.5px;border-bottom:1px solid var(--date-line);display:flex;align-items:center;justify-content:center;gap:4px;font-size:14px}
.meta-row:last-child{border-bottom:none}
.post-image{width:312px;height:169px;border-radius:3px;background:linear-gradient(180deg,#a9c4e6 0%,#b6b49c 30%,#8f9a76 50%,#d9cdb0 70%,#3ea6c9 85%,#2a8fbf 100%)}
.post-body{width:320px}
.post-title{font-family:'Arvo',serif;font-size:16.5px;color:var(--ink);line-height:1}
.post-text{font-size:12px;line-height:14px;color:var(--muted);margin-top:7px}
.post-more{font-size:12px;font-weight:600;color:var(--text);margin-top:17px}

/* footer */
.footer{left:0;top:932px;width:1092px;height:235px;background:var(--footer)}
.footer-bottom{left:0;top:1167px;width:1092px;height:33px;background:var(--footer-bottom);color:var(--footer-text);font-size:10px;text-align:center;line-height:33px}
.f-head{font-family:'Arvo',serif;font-size:12.5px;color:var(--footer-head);letter-spacing:.3px}
.f-head::after{content:"";display:block;width:29px;height:2px;background:var(--accent);margin-top:7px}
.f-tag{font-size:10.5px;font-weight:700;color:var(--accent-text)}
.f-item{display:flex;gap:10px;font-size:10px;line-height:11px;color:var(--footer-text);align-items:flex-start}
.f-item svg{flex:none;margin-top:1px}
.listing{display:flex;gap:21px;width:230px}
.listing-thumb{width:44px;height:44px;border-radius:4px;background:#3a3a3a;display:flex;align-items:center;justify-content:center;flex:none}
.listing-text{font-size:10px;line-height:11px;color:var(--footer-text);padding-top:3px}
.listing-price{color:var(--accent-text);font-size:11.5px;margin-top:2px}
.field{background:var(--footer-field);color:var(--footer-text);font-size:9.5px;padding:6px 6px}
.submit{left:823px;top:1116px;width:111px;height:31px;background:var(--accent);color:var(--white);font-size:13px;font-weight:700;text-align:center;line-height:31px}
.float-btn{width:46px;height:45px;background:var(--accent);display:flex;align-items:center;justify-content:center}
</style>
</head>
<body>
<div class="abs top-rule"></div>

<!-- Team -->
<h1 class="abs section-title" style="top:50px">Meet Our Team</h1>
<p class="abs section-sub" style="top:94px">Lorem Ipsum is simply dummy text of the printing and typesetting industry.</p>

<svg class="abs team-shapes" width="1092" height="317" viewBox="0 160 1092 317" aria-hidden="true">
  <polygon points="291,204 524,164 524,477 291,477" fill="var(--panel)"/>
  <polygon points="524,163 534,163 534,477 524,477" fill="var(--panel-stripe)"/>
  <polygon points="558,163 568,163 568,477 558,477" fill="var(--panel-stripe)"/>
  <polygon points="568,164 801,204 801,477 568,477" fill="var(--panel)"/>
</svg>

<div class="abs photo photo-left" role="img" aria-label="Portrait of a team member in a tweed jacket, arms crossed"></div>
<div class="abs photo photo-right" role="img" aria-label="Portrait of team member Nora Hale in a blush blazer"></div>

<div class="abs member" style="left:312px;top:212px">
  <h2 class="member-name">Pat................</h2>
  <p class="member-bio">It is a long established fact that<br>a reader will be distracted by<br>the readable content of a page<br>when looking at its layout. The<br>point of using Lorem Ipsum is<br>that it has a more-or-less<br>normal distribution of letters,<br>as opposed to using '.</p>
  <p class="member-more">Read more...</p>
  <div class="socials" aria-label="Social profiles"><span></span><span></span><span></span></div>
</div>
<div class="abs member" style="left:575px;top:212px">
  <h2 class="member-name">Nora Hale</h2>
  <p class="member-bio">It is a long established fact that<br>a reader will be distracted by<br>the readable content of a page<br>when looking at its layout. The<br>point of using Lorem Ipsum is<br>that it has a more-or-less<br>normal distribution of letters,<br>as opposed to using '.</p>
  <p class="member-more">Read more...</p>
  <div class="socials" aria-label="Social profiles"><span></span><span></span><span></span></div>
</div>

<!-- Blog -->
<div class="abs blog" role="img" aria-label="Soft beach backdrop with palm trees, sky and ocean"></div>
<h2 class="abs section-title" style="top:524px">Latest Blog</h2>
<p class="abs section-sub" style="top:571px">Lorem Ipsum is simply dummy text of the printing and typesetting industry.</p>

<div class="abs post-meta" style="left:158px;top:616px">
  <div class="meta-date"><div class="meta-day">28</div><div class="meta-month">feb</div></div>
  <div class="meta-row">32 <svg width="14" height="12" viewBox="0 0 14 12"><path d="M7 11 L1.8 6 A3 3 0 0 1 7 2.2 A3 3 0 0 1 12.2 6 Z" fill="none" stroke="#fff" stroke-width="1.1"/></svg></div>
  <div class="meta-row">50 <svg width="14" height="12" viewBox="0 0 14 12"><path d="M1 2 H13 V8 H6 L3 11 V8 H1 Z" fill="none" stroke="#fff" stroke-width="1.1"/></svg></div>
  <div class="meta-row"><svg width="14" height="14" viewBox="0 0 14 14"><circle cx="3" cy="7" r="2" fill="#fff"/><circle cx="11" cy="3" r="2" fill="#fff"/><circle cx="11" cy="11" r="2" fill="#fff"/><path d="M3 7 L11 3 M3 7 L11 11" stroke="#fff" stroke-width="1.2"/></svg></div>
</div>
<div class="abs post-image" style="left:224px;top:616px" role="img" aria-label="Hillside homes above a sandy cove and turquoise ocean"></div>
<div class="abs post-body" style="left:224px;top:802px">
  <h3 class="post-title">Lorem Ipsum is simply dummy text</h3>
  <p class="post-text">Contrary to popular belief, Lorem Ipsum is not simply random text. It has roots in a piece of classical Latin literature from 45 BC, making it over 2000 years old.</p>
  <p class="post-more">Read more..</p>
</div>

<div class="abs post-meta" style="left:556px;top:616px">
  <div class="meta-date"><div class="meta-day">28</div><div class="meta-month">feb</div></div>
  <div class="meta-row">32 <svg width="14" height="12" viewBox="0 0 14 12"><path d="M7 11 L1.8 6 A3 3 0 0 1 7 2.2 A3 3 0 0 1 12.2 6 Z" fill="none" stroke="#fff" stroke-width="1.1"/></svg></div>
  <div class="meta-row">50 <svg width="14" height="12" viewBox="0 0 14 12"><path d="M1 2 H13 V8 H6 L3 11 V8 H1 Z" fill="none" stroke="#fff" stroke-width="1.1"/></svg></div>
  <div class="meta-row"><svg width="14" height="14" viewBox="0 0 14 14"><circle cx="3" cy="7" r="2" fill="#fff"/><circle cx="11" cy="3" r="2" fill="#fff"/><circle cx="11" cy="11" r="2" fill="#fff"/><path d="M3 7 L11 3 M3 7 L11 11" stroke="#fff" stroke-width="1.2"/></svg></div>
</div>
<div class="abs post-image" style="left:622px;top:616px" role="img" aria-label="Hillside homes above a sandy cove and turquoise ocean"></div>
<div class="abs post-body" style="left:622px;top:802px">
  <h3 class="post-title">Lorem Ipsum is simply dummy text</h3>
  <p class="post-text">Contrary to popular belief, Lorem Ipsum is not simply random text. It has roots in a piece of classical Latin literature from 45 BC, making it over 2000 years old.</p>
  <p class="post-more">Read more..</p>
</div>

<!-- Footer -->
<div class="abs footer"></div>

<h4 class="abs f-head" style="left:158px;top:961px">FIND US</h4>
<p class="abs f-tag" style="left:158px;top:992px">The standard Lorem Ipsum passage</p>
<div class="abs f-item" style="left:158px;top:1016px;width:170px">
  <svg width="10" height="13" viewBox="0 0 10 13"><path d="M5 12 C2 8 1 6.5 1 5 A4 4 0 0 1 9 5 C9 6.5 8 8 5 12 Z" fill="none" stroke="#ddd" stroke-width="1"/><circle cx="5" cy="5" r="1.4" fill="none" stroke="#ddd"/></svg>
  <span>TLorem Ipsum is simply dummy text of the printing</span>
</div>
<div class="abs f-item" style="left:158px;top:1051px">
  <svg width="11" height="11" viewBox="0 0 11 11"><path d="M2 1 L4 3 L3 4.5 C4 6.5 5 7.5 6.5 8 L8 7 L10 9 L8.5 10.5 C5 10 1 6 0.5 2.5 Z" fill="none" stroke="#ddd" stroke-width="1"/></svg>
  <span>(00) 12-345-6789</span>
</div>
<div class="abs f-item" style="left:158px;top:1074px">
  <svg width="11" height="9" viewBox="0 0 11 9"><rect x=".5" y=".5" width="10" height="8" fill="none" stroke="#ddd"/><path d="M.5 .5 L5.5 5 L10.5 .5" fill="none" stroke="#ddd"/></svg>
  <span>info@containing Lorem Ipsum</span>
</div>

<h4 class="abs f-head" style="left:358px;top:961px">FEATURED LISTINGS</h4>
<div class="abs listing" style="left:358px;top:991px">
  <div class="listing-thumb" role="img" aria-label="Listing photo"><svg width="24" height="20" viewBox="0 0 24 20"><rect x="1" y="1" width="22" height="18" fill="none" stroke="#666" stroke-width="2"/><path d="M4 16 L10 9 L14 13 L17 10 L21 16 Z" fill="#666"/><circle cx="16" cy="6" r="2" fill="#666"/></svg></div>
  <div class="listing-text">Lorem Ipsum is simply dummy text of the printing and typesetting<div class="listing-price">$35,000,000</div></div>
</div>
<div class="abs listing" style="left:358px;top:1046px">
  <div class="listing-thumb" role="img" aria-label="Listing photo"><svg width="24" height="20" viewBox="0 0 24 20"><rect x="1" y="1" width="22" height="18" fill="none" stroke="#666" stroke-width="2"/><path d="M4 16 L10 9 L14 13 L17 10 L21 16 Z" fill="#666"/><circle cx="16" cy="6" r="2" fill="#666"/></svg></div>
  <div class="listing-text">Lorem Ipsum is simply dummy text of the printing and typesetting<div class="listing-price">$35,000,000</div></div>
</div>
<div class="abs listing" style="left:358px;top:1101px">
  <div class="listing-thumb" role="img" aria-label="Listing photo"><svg width="24" height="20" viewBox="0 0 24 20"><rect x="1" y="1" width="22" height="18" fill="none" stroke="#666" stroke-width="2"/><path d="M4 16 L10 9 L14 13 L17 10 L21 16 Z" fill="#666"/><circle cx="16" cy="6" r="2" fill="#666"/></svg></div>
  <div class="listing-text">Lorem Ipsum is simply dummy text of the printing and typesetting<div class="listing-price">$35,000,000</div></div>
</div>

<h4 class="abs f-head" style="left:622px;top:961px">CONTACT US</h4>
<div class="abs field" style="left:622px;top:992px;width:312px;height:25px">Name:</div>
<div class="abs field" style="left:622px;top:1023px;width:179px;height:24px">Email:</div>
<div class="abs field" style="left:813px;top:1023px;width:121px;height:24px">Phone:</div>
<div class="abs field" style="left:622px;top:1054px;width:312px;height:51px">Massage:</div>
<div class="abs submit">Submit</div>

<div class="abs float-btn" style="left:975px;top:961px" aria-label="Email us">
  <svg width="20" height="14" viewBox="0 0 20 14"><rect x=".75" y=".75" width="18.5" height="12.5" fill="none" stroke="#fff" stroke-width="1.3"/><path d="M.75 .75 L10 8 L19.25 .75" fill="none" stroke="#fff" stroke-width="1.3"/></svg>
</div>
<div class="abs float-btn" style="left:1034px;top:961px" aria-label="Back to top">
  <svg width="18" height="10" viewBox="0 0 18 10"><path d="M1 9 L9 1 L17 9" fill="none" stroke="#fff" stroke-width="1.5"/></svg>
</div>

<div class="abs footer-bottom">Copyright © 2015. All Rights Reserved. Terms &amp; Conditions</div>
</body>
</html>
```